Buch-/E-Book-Cover für einen Eltern-Ratgeber
Zielgruppe
Ich bin Autor/Self-Publisher von Büchern/E-Books.
Aufgabenstellung
Ich benötige ein Buchcover (Print Paperback und E-Book) für einen kurzen Eltern-Ratgeber (ca. 60 Seiten):
Titel: 'Kleine Helden im Badezimmer'
Autorin: Frieda Wolkenstein
FW Verlag, Berlin
Das Buch richtet sich an verzweifelte Eltern und gibt Tipps, wie sie ihre kleinen Kinder zum Zähne putzen animieren können. Für die Gestaltung gerne vorzugsweise Fotos von echten Menschen (Eltern + Kind bzw. nur Kind bzw. 2 Kinder). Illustrierte Cover sind auch OK, aber nicht präferiert. Für Vorschläge bitte *inklusive Rückseite* und an bestehenden Eltern-Ratgebern orientieren, die Buchhafen zu finden sind, wie zum Beispiel:
- Wiegenzeit von Tilo K. Brenner
- PAPA im Takt von Nora Fendt
- Mutig durch den Alltag von Wiebke Tolan
- Grenzen setzen ohne Streit von Gudrun Vell-Borm
Auf den Buchseiten sind Illustrationen enthalten, die mit dem Buchcover möglichst auch harmonisieren sollten. Die Entwürfe der Illustrationen sind hier hochgeladen.
Ggf. kann man mit einer Text-Banderole/Kreis arbeiten, mit der Aufschrift '21 praktische Tipps für Eltern'
Klappentext:
Ihr Kind will sich partout nicht die Zähne putzen? Jedes Bitten und Flehen sind vergebens?
Für viele Eltern von kleinen Kindern ist es ein täglicher K(r)ampf im Bad. Ein ewiges Theater und langes Diskutieren. Niemand möchte sein Kind zwingen, schon gar nicht körperlich. Aber ohne Zähneputzen keine gesunden und schönen Zähne. Was also tun?
Nicht verzweifeln! Alle geplagten Eltern von Zwei- bis Fünfjährigen finden in diesem Büchlein 21 kurze und praktische Tipps, wie sie ihr Kind zum Zähneputzen animieren können. So wird das Zähneputzen ein fester Bestandteil der Morgen- und Abendroutine. Mit Spaß und Freude und ohne Graus. Probieren Sie die Tipps heute noch aus!

```html
<!DOCTYPE html>
<html lang="de">
<head>
<meta charset="utf-8">
<title>Kleine Helden im Badezimmer – Cover</title>
<link rel="stylesheet" href="https://fonts.googleapis.com/css2?family=Barlow:wght@500;600&family=Oswald:wght@600&family=Damion&family=Roboto+Condensed:wght@400&display=swap">
<style>
  :root {
    --page-bg: #f2f2f3;
    --cover-top: #eef5f8;
    --cover-bottom: #f4f2f4;
    --brown: #6a4d4b;
    --brown-dark: #553838;
    --purple: #a65fa6;
    --purple-deep: #95509a;
    --text: #3a2f2f;
    --white: #ffffff;
  }
  * { box-sizing: border-box; margin: 0; padding: 0; }
  html, body { width: 1200px; height: 1195px; overflow: hidden; }
  body { background: var(--page-bg); position: relative; }

  .cover {
    position: absolute;
    top: 207px;
    width: 540px;
    height: 780px;
    background: linear-gradient(180deg, var(--cover-top) 0%, var(--cover-bottom) 100%);
    overflow: hidden;
    box-shadow: 0 18px 40px rgba(0,0,0,0.12);
  }
  .cover--front { left: 40px; }
  .cover--back { left: 620px; }

  .author {
    position: absolute; top: 40px; width: 100%;
    text-align: center;
    font-family: "Barlow", sans-serif; font-weight: 600;
    font-size: 18px; letter-spacing: 1px; color: var(--brown);
  }
  .title-main {
    position: absolute; top: 70px; width: 100%;
    text-align: center;
    font-family: "Oswald", sans-serif; font-weight: 600;
    font-size: 66px; color: var(--brown); letter-spacing: -0.5px;
  }
  .title-script {
    position: absolute; top: 158px; width: 100%;
    text-align: center;
    font-family: "Damion", cursive;
    font-size: 64px; color: var(--purple);
  }
  .photo {
    position: absolute; left: 0; right: 0; top: 250px; bottom: 0;
    background:
      radial-gradient(ellipse at 40% 40%, #f3d7c6 0%, rgba(243,215,198,0) 45%),
      radial-gradient(ellipse at 70% 30%, #dcb98a 0%, rgba(220,185,138,0) 50%),
      linear-gradient(180deg, rgba(238,245,248,0) 0%, #e9c9cf 55%, #eed0dc 100%);
  }
  .tips-badge {
    position: absolute; left: 115px; top: 614px;
    width: 150px; height: 150px; border-radius: 50%;
    background: var(--brown-dark); color: var(--white);
    text-align: center;
    font-family: "Barlow", sans-serif;
  }
  .tips-badge .num { display: block; margin-top: 12px; font-size: 48px; font-weight: 600; line-height: 1; }
  .tips-badge .word { display: block; font-size: 20px; font-weight: 500; line-height: 1.2; }
  .tips-badge .tips { display: block; font-size: 34px; font-weight: 600; line-height: 1; }
  .audience-band {
    position: absolute; left: 255px; top: 650px;
    width: 230px; height: 72px;
    background: var(--purple-deep);
    transform: rotate(-3deg);
    color: var(--white);
    font-family: "Damion", cursive; font-size: 48px;
    text-align: center; line-height: 72px;
  }

  .blurb {
    position: absolute; top: 85px; left: 50px; right: 50px;
    text-align: center; color: var(--text);
  }
  .blurb-lead {
    font-family: "Barlow", sans-serif; font-weight: 600;
    font-size: 19px; letter-spacing: 1px; line-height: 1.4;
    color: var(--brown-dark);
  }
  .blurb-body {
    margin-top: 28px;
    font-family: "Roboto Condensed", sans-serif;
    font-size: 16px; line-height: 1.5;
  }
  .blurb-accent {
    margin-top: 16px;
    font-family: "Damion", cursive; font-size: 44px; color: var(--purple);
  }
  .blurb-close {
    margin-top: 34px;
    font-family: "Barlow", sans-serif; font-weight: 600;
    font-size: 18px; letter-spacing: 1px; line-height: 1.35;
    color: var(--brown-dark);
  }
</style>
</head>
<body>
  <section class="cover cover--front">
    <div class="photo" role="img" aria-label="Foto: Mutter und kleine Tochter im rosa Bademantel putzen lachend gemeinsam Zähne"></div>
    <p class="author">Frieda Wolkenstein</p>
    <h1 class="title-main">Kleine Helden</h1>
    <p class="title-script">im Badezimmer</p>
    <div class="tips-badge">
      <span class="num">21</span>
      <span class="word">praktische</span>
      <span class="tips">TIPPS</span>
    </div>
    <div class="audience-band">für Eltern</div>
  </section>

  <section class="cover cover--back">
    <div class="blurb">
      <p class="blurb-lead">Ihr Kind will sich partout nicht die Zähne putzen? Jedes Bitten und Flehen ist vergebens?</p>
      <p class="blurb-body">Für viele Eltern von kleinen Kindern ist es ein täglicher K(r)ampf im Bad. Ein ewiges Theater und langes Diskutieren. Niemand möchte sein Kind zwingen, schon gar nicht körperlich. Aber ohne Zähneputzen keine gesunden und schönen Zähne. Was also tun?</p>
      <p class="blurb-accent">Nicht verzweifeln!</p>
      <p class="blurb-body" style="margin-top:14px">Alle geplagten Eltern von Zwei- bis Fünfjährigen finden in diesem Büchlein 21 kurze und praktische Tipps, wie sie Ihr Kind zum Zähneputzen animieren können. So wird das Zähneputzen ein fester Bestandteil der Morgen- und Abendroutine. Mit Spaß und Freude und ohne Graus.</p>
      <p class="blurb-close">Probieren Sie die Tipps<br>heute noch aus!</p>
    </div>
  </section>
</body>
</html>
```